LABEL for Extra Virgin Olive oil

Hi everyone!
I would please like your help with the below project.

We will start importing olive oil from Greece and I would like to create the label for the bottle.
Our goal is to create a label that will really promote the raw quality of the natural product (olive oil).
The olive oil we will import will be very high quality, but we don't want the label to promote a luxury product but more just an exceptional quality natural product that is for the many and comes directly from the producer. Potentially the label can also include images (ex. oils, olive trees, land, sea, sun) but we can evaluate that along the way.
The approximate size of the label will be 60x110 mm
The colors should be earth colors
We can discuss any potential questions as soon as we are in contact.

Thank you all in advance for your time and consideration.

Kind regards, Tobias

```html
<!DOCTYPE html>
<html lang="en">
<head>
<meta charset="utf-8">
<title>Extra Virgin Olive Oil Label</title>
<link href="https://fonts.googleapis.com/css2?family=Cinzel:wght@700&family=Quicksand:wght@500;700&family=Yellowtail&family=Roboto+Condensed:wght@500&display=swap" rel="stylesheet">
<style>
  :root {
    --page: #ffffff;
    --label-black: #1b1b1d;
    --label-edge: #111113;
    --gold-light: #e8d3a2;
    --gold: #c9ab72;
    --gold-deep: #9c7d45;
    --cream: #f1ead8;
  }
  * { margin: 0; padding: 0; box-sizing: border-box; }
  html, body {
    width: 900px;
    height: 1200px;
    overflow: hidden;
    background: var(--page);
  }
  .label {
    position: absolute;
    left: 190px;
    top: 50px;
    width: 520px;
    height: 1100px;
    background: linear-gradient(90deg, var(--label-edge) 0%, var(--label-black) 12%, var(--label-black) 88%, var(--label-edge) 100%);
    overflow: hidden;
  }
  .tree-emblem {
    position: absolute;
    left: 174px;
    top: 80px;
    width: 172px;
    height: 210px;
    border-radius: 50% 50% 10% 10%;
    background: radial-gradient(ellipse at 50% 40%, var(--gold) 0%, var(--gold-deep) 60%, rgba(156,125,69,0.15) 100%);
  }
  .premium {
    position: absolute;
    left: 0; right: 0;
    top: 318px;
    text-align: center;
    font-family: "Cinzel", serif;
    font-weight: 700;
    font-size: 52px;
    letter-spacing: 1px;
    color: var(--gold-light);
  }
  .natural {
    position: absolute;
    left: 0; right: 0;
    top: 380px;
    text-align: center;
    font-family: "Quicksand", sans-serif;
    font-weight: 500;
    font-size: 27px;
    color: var(--cream);
  }
  .olive-emblem {
    position: absolute;
    left: 88px;
    top: 462px;
    width: 345px;
    height: 258px;
  }
  .product-name {
    position: absolute;
    left: 0; right: 0;
    top: 735px;
    text-align: center;
    font-family: "Yellowtail", cursive;
    font-size: 120px;
    line-height: 1.1;
    color: var(--gold-light);
  }
  .grade {
    position: absolute;
    left: 0; right: 0;
    top: 918px;
    display: flex;
    align-items: center;
    justify-content: center;
    gap: 16px;
    font-family: "Quicksand", sans-serif;
    font-weight: 700;
    font-size: 31px;
    letter-spacing: 1px;
    color: var(--gold);
  }
  .grade .rule {
    width: 70px;
    height: 2px;
    background: var(--gold);
  }
  .net-volume {
    position: absolute;
    left: 126px;
    top: 1004px;
    width: 268px;
    height: 58px;
    border: 2px solid var(--cream);
    border-bottom: none;
    border-radius: 22px 22px 0 0;
    text-align: center;
    padding-top: 12px;
    font-family: "Roboto Condensed", sans-serif;
    font-weight: 500;
    font-size: 24px;
    color: var(--cream);
  }
  .gold-band {
    position: absolute;
    left: 0; right: 0;
    bottom: 0;
    height: 36px;
    background: linear-gradient(90deg, var(--gold-deep), var(--gold-light) 30%, var(--gold) 60%, var(--gold-light) 85%, var(--gold-deep));
  }
  .gold-band::before {
    content: "";
    position: absolute;
    left: 0; right: 0;
    top: -10px;
    height: 10px;
    background: linear-gradient(180deg, rgba(201,171,114,0) 0%, rgba(201,171,114,0.55) 100%);
  }
</style>
</head>
<body>
  <main class="label">
    <div class="tree-emblem" role="img" aria-label="Gold illustration of an olive tree with spreading branches and roots"></div>
    <h1 class="premium">PREMIUM</h1>
    <p class="natural">100% Naturol</p>
    <div class="olive-emblem" role="img" aria-label="Gold illustration of two olives hanging beneath a sprig of leaves">
      <svg width="345" height="258" viewBox="0 0 345 258" aria-hidden="true">
        <defs>
          <radialGradient id="oliveTone" cx="50%" cy="45%" r="60%">
            <stop offset="0%" stop-color="#e8d3a2"/>
            <stop offset="100%" stop-color="#b8955a"/>
          </radialGradient>
        </defs>
        <ellipse cx="172" cy="160" rx="120" ry="95" fill="url(#oliveTone)" opacity="0.9"/>
      </svg>
    </div>
    <h2 class="product-name">Olive Oil</h2>
    <p class="grade"><span class="rule"></span>EXTRA VIRGIN<span class="rule"></span></p>
    <p class="net-volume">Net 8.5 fl oz (250 ml)</p>
    <div class="gold-band"></div>
  </main>
</body>
</html>
```